Business Stationary & Card Design

Double sided business cards, letterhead, horizontal brochure, and envelope design using our logo. We want a modern minimal look. One side of the business card should be only our logo and maybe our slogan "Get It Done Right". The other side should include our coil spring and not the logo again. Watermark like (or not) positioned partially, horizontal, on angle, or a combination of. IF a background color or accent color is used we like blue (4885ed). The letterhead, brochure, and envelope design should be similar to the card. Except no solid background color.Maybe the spring at the bottom of the letterhead page watermark style and partial. Additional info on the business card should be present:
Employee Name
Position
Phone
Email
Address
The final design should communicate strength, simplicity, and newness.

Target Market(s)

35-55 Male & Female

Industry/Entity Type

Automotive

Contact Information for Business Card

One side of the double sided business card should be only our logo and maybe our slogan "Get It Done Right". The other side should include our coil spring and not the logo again. Watermark like (or not) positioned partially, horizontal, on angle, or a combination of. IF a background color or accent color is used we like blue (4885ed). Additional info on the business card should be present:
Employee Name
Position
Phone
Email
Address

Font styles to use
Other font styles liked:
• Use font that compliments the attached font. Maybe plain eurostyle?

Colors
0492cd
3276b5

Requirements
Must have
• Use the coil spring in a subtle unique way (s). Double sided business card
Should not have
• Clutter, colors that do not coordinate well with our logo. Fonts that do not compliment our font.

```html
<!DOCTYPE html>
<html lang="en">
<head>
<meta charset="utf-8">
<title>Coilfast Motors Stationery Set</title>
<link rel="stylesheet" href="https://fonts.googleapis.com/css2?family=Michroma&display=swap">
<style>
  :root{
    --stage:#2a2d2f;
    --brand-blue:#2d77b7;
    --brand-yellow:#e0be24;
    --ink:#1c1c1c;
    --paper:#ffffff;
    --cream:#f8f1da;
  }
  *{box-sizing:border-box;margin:0;padding:0}
  html,body{width:1200px;height:1200px;overflow:hidden;background:var(--stage)}
  body{position:relative;font-family:"Michroma",sans-serif}
  .piece{position:absolute}
  .wordmark{font-family:"Michroma",sans-serif;color:var(--brand-yellow);white-space:nowrap;letter-spacing:.02em}
  .contact{list-style:none;color:var(--paper);font-size:7px;line-height:1.5;letter-spacing:.02em;white-space:nowrap}
  .contact li{display:flex;align-items:flex-start;gap:4px}
  .contact svg{width:7px;height:7px;flex:none;margin-top:1px}
  .rot-ccw{position:absolute;transform-origin:0 0;transform:rotate(-90deg);white-space:nowrap}
  .flip{position:absolute;transform:rotate(180deg)}

  /* large envelope */
  .envelope-large{left:107px;top:67px;width:472px;height:746px}
  .envelope-large .flap{position:absolute;left:0;top:0;width:100%;height:80px}
  .envelope-large .body{position:absolute;left:0;top:78px;width:100%;height:668px;background:var(--brand-blue)}

  /* small envelope */
  .envelope-small{left:106px;top:846px;width:474px;height:288px}
  .envelope-small .flap{position:absolute;left:0;top:0;width:100%;height:72px}
  .envelope-small .body{position:absolute;left:0;top:70px;width:100%;height:218px;background:var(--brand-blue)}

  /* cards */
  .card-front{left:702px;top:78px;width:340px;height:194px;background:var(--brand-blue)}
  .card-front .frame{position:absolute;left:22px;top:23px;width:294px;height:145px;border:1px solid var(--brand-yellow)}
  .card-front .slogan{left:309px;top:154px;color:var(--paper);font-size:7px;line-height:12px;letter-spacing:.08em;background:var(--brand-blue);padding:0 5px}
  .card-back{left:702px;top:284px;width:340px;height:194px;background:var(--paper)}
  .card-back .coil{position:absolute;left:16px;top:14px;width:90px;height:168px;background:var(--cream);border-radius:14px}
  .card-back .name{position:absolute;left:148px;top:54px;font-size:15px;color:var(--ink);letter-spacing:.03em;white-space:nowrap}
  .card-back .name b{color:var(--brand-blue);font-weight:400}
  .card-back .role{position:absolute;left:148px;top:74px;font-size:6.5px;color:var(--ink)}
  .card-back .details{position:absolute;left:148px;top:95px;font-size:6.5px;color:var(--ink);border-collapse:collapse;white-space:nowrap}
  .card-back .details th{color:var(--brand-blue);font-weight:400;text-align:left;padding:0 6px 5px 0;vertical-align:top}
  .card-back .details td{padding:0 0 5px 0;vertical-align:top}

  /* letterhead */
  .letterhead{left:652px;top:502px;width:440px;height:624px;background:var(--paper)}
  .letterhead .contact{position:absolute;left:260px;top:30px;color:var(--ink)}
  .letterhead .coil{position:absolute;left:60px;top:522px;width:320px;height:102px;background:var(--cream);border-radius:40px 40px 0 0}
</style>
</head>
<body>

<svg width="0" height="0" style="position:absolute" aria-hidden="true">
  <symbol id="icon-phone" viewBox="0 0 10 10"><rect x=".5" y=".5" width="9" height="9" rx="2" fill="none" stroke="#e0be24"/><path d="M3 2.5l1 1.5-.7.8a4 4 0 0 0 2 2l.8-.7 1.5 1-.6 1C4.5 8 2 5.5 2 3.2z" fill="#e0be24"/></symbol>
  <symbol id="icon-mail" viewBox="0 0 10 10"><rect x=".5" y=".5" width="9" height="9" rx="2" fill="none" stroke="#e0be24"/><path d="M2.5 3.2h5v3.6h-5zM2.5 3.2L5 5.2l2.5-2" fill="none" stroke="#e0be24" stroke-width=".8"/></symbol>
  <symbol id="icon-pin" viewBox="0 0 10 10"><path d="M5 9.5S1.8 6 1.8 4a3.2 3.2 0 0 1 6.4 0C8.2 6 5 9.5 5 9.5z" fill="none" stroke="#e0be24"/><circle cx="5" cy="4" r="1.1" fill="#e0be24"/></symbol>
</svg>

<!-- Large envelope -->
<section class="piece envelope-large" aria-label="Large envelope">
  <svg class="flap" viewBox="0 0 472 80" preserveAspectRatio="none"><path d="M0 80 L16 10 Q18 0 30 0 H442 Q454 0 456 10 L472 80 Z" fill="var(--brand-yellow)"/></svg>
  <div class="flip wordmark" style="left:176px;top:24px;font-size:13px;color:var(--paper)">COILFAST MOTORS</div>
  <div class="body"></div>
  <ul class="contact rot-ccw" style="left:33px;top:286px">
    <li><svg><use href="#icon-phone"/></svg>000.000.000</li>
    <li><svg><use href="#icon-mail"/></svg>INFO@COILFASTMOTORS.COM</li>
    <li><svg><use href="#icon-pin"/></svg>STREET ADDRESS HERE,<br>USA, 2476</li>
  </ul>
  <div class="rot-ccw wordmark" style="left:396px;top:705px;font-size:24px">COILFAST</div>
  <div class="rot-ccw wordmark" style="left:426px;top:705px;font-size:10px;color:var(--paper);letter-spacing:.5em">MOTORS</div>
</section>

<!-- Small envelope -->
<section class="piece envelope-small" aria-label="Small envelope">
  <svg class="flap" viewBox="0 0 474 72" preserveAspectRatio="none"><path d="M0 72 L16 10 Q18 0 30 0 H444 Q456 0 458 10 L474 72 Z" fill="var(--brand-yellow)"/></svg>
  <div class="flip wordmark" style="left:190px;top:24px;font-size:11px;color:var(--paper)">COILFAST MOTORS</div>
  <div class="body"></div>
  <ul class="contact" style="position:absolute;left:327px;top:92px">
    <li><svg><use href="#icon-phone"/></svg>000.000.000</li>
    <li><svg><use href="#icon-mail"/></svg>INFO@COILFASTMOTORS.COM</li>
    <li><svg><use href="#icon-pin"/></svg>STREET ADDRESS HERE,<br>USA, 2476</li>
  </ul>
  <div class="wordmark" style="position:absolute;left:24px;top:243px;font-size:11px">COILFAST MOTORS</div>
</section>

<!-- Business card front -->
<section class="piece card-front" aria-label="Business card front">
  <div class="frame"></div>
  <div class="wordmark" style="position:absolute;left:22px;top:88px;font-size:12px;line-height:24px;background:var(--brand-blue);padding-right:6px">COILFAST MOTORS</div>
  <div class="slogan rot-ccw">GET IT DONE RIGHT</div>
</section>

<!-- Business card back -->
<section class="piece card-back" aria-label="Business card back">
  <div class="coil" role="img" aria-label="Faint coil spring watermark"></div>
  <p class="name"><b>DANA</b> REYES</p>
  <p class="role">MARKETING MANAGER</p>
  <table class="details">
    <tr><th>TEL</th><td>: 000.000.000</td></tr>
    <tr><th>EMAIL</th><td>: INFO@COILFASTMOTORS.COM</td></tr>
    <tr><th>ADD</th><td>: STREET ADDRESS HERE,<br>&nbsp; USA, 2476</td></tr>
  </table>
</section>

<!-- Letterhead -->
<section class="piece letterhead" aria-label="Letterhead">
  <div class="wordmark" style="position:absolute;left:33px;top:46px;font-size:11px">COILFAST MOTORS</div>
  <ul class="contact">
    <li><svg><use href="#icon-phone"/></svg>000.000.000</li>
    <li><svg><use href="#icon-mail"/></svg>INFO@COILFASTMOTORS.COM</li>
    <li><svg><use href="#icon-pin"/></svg>STREET ADDRESS HERE,<br>USA, 2476</li>
  </ul>
  <div class="coil" role="img" aria-label="Partial coil spring watermark along the bottom edge"></div>
</section>

</body>
</html>
```